Business Card for Multi-Brand Sportswear Company

We are looking for a business card which represents our company and the multiple brands within it.

The company: Kelt Athletic (LTD)
The brands: Kelt, PawaLuni, VerdantFlex, Grit and Gale

Employees using these cards would be representing Kelt Athletic, rather than any of the individual brands. You will see a current design within the uploaded files, to give some inspiration. The actual text of the brands is not necessary, but the logos should be on there is some format.

Our creative minds on this are stretched, so we are looking for someone to make this their own, and show us what a good business card should look like.

We may like to get these printed with spot gloss, so keep that in mind with your designs.

www.keltathletic.co.uk

Industry/Entity Type

Business

Contact Information for Business Card

Tom Hollingsworth-Pryce
Operations Manager
(+44) 1632 960 418
Tom@keltathletic.co.uk
www.keltathletic.co.uk

Font styles to use
Sans Serif
Other font styles liked:
• Eurostile

Colors
ffffff

Requirements
Nice to have
• Dark (black) background

```html
<!DOCTYPE html>
<html lang="en">
<head>
<meta charset="utf-8">
<title>Kelt Athletic – Business Card</title>
<link href="https://fonts.googleapis.com/css2?family=Open+Sans:wght@400;600&display=swap" rel="stylesheet">
<style>
  :root {
    --page: #ecebe8;
    --card-white: #f7f7f7;
    --card-black: #2b2a29;
    --ink: #1d1d1d;
    --red: #c8181e;
    --muted: #6e6e6e;
    --gloss: #5a5958;
    --plum: #6b5a7b;
  }
  * { margin: 0; padding: 0; box-sizing: border-box; }
  html, body { width: 1200px; height: 801px; overflow: hidden; }
  body {
    background: var(--page);
    font-family: "Open Sans", sans-serif;
    color: var(--ink);
    position: relative;
  }
  .card {
    position: absolute;
    top: 236px;
    width: 510px;
    height: 329px;
    border-radius: 3px;
    box-shadow: 0 2px 6px rgba(0,0,0,0.12);
  }
  .card-front { left: 62px; background: var(--card-white); }
  .card-back { left: 628px; background: var(--card-black); display: flex; align-items: center; justify-content: center; }

  .name-block { position: absolute; left: 34px; top: 34px; padding-left: 14px; border-left: 5px solid var(--red); }
  .person-name { font-size: 24px; font-weight: 400; letter-spacing: 0.2px; line-height: 1.1; }
  .person-name .surname-end { color: var(--red); }
  .job-title { font-size: 14px; color: var(--red); margin-top: 2px; }

  .contact-list { position: absolute; left: 38px; top: 112px; list-style: none; }
  .contact-list li { display: flex; align-items: center; gap: 12px; font-size: 16px; line-height: 28px; }
  .contact-list svg { width: 16px; height: 16px; flex: none; }

  .company-mark { position: absolute; right: 34px; top: 150px; display: flex; align-items: center; gap: 8px; }
  .company-mark .mark-dot { width: 14px; height: 14px; background: var(--red); }
  .company-mark .mark-name { font-size: 20px; font-weight: 600; color: var(--ink); }

  .brand-row { position: absolute; left: 34px; right: 34px; bottom: 34px; display: flex; justify-content: space-between; align-items: center; }
  .brand { display: flex; align-items: center; gap: 6px; font-size: 13px; font-weight: 600; }
  .brand-pawaluni { color: var(--plum); }
  .brand-pawaluni .brand-shape { width: 12px; height: 12px; background: var(--plum); }
  .brand-grit { color: var(--red); }
  .brand-grit .brand-shape { width: 12px; height: 12px; border-radius: 50%; background: var(--red); }
  .brand-kelt { color: var(--ink); }
  .brand-verdant { color: var(--muted); }
  .brand-verdant .brand-shape { width: 12px; height: 12px; border-radius: 50%; border: 2px solid var(--muted); }

  .back-mark { display: flex; align-items: center; gap: 12px; }
  .back-mark .mark-dot { width: 22px; height: 22px; background: var(--gloss); }
  .back-mark .mark-name { font-size: 34px; font-weight: 600; color: var(--gloss); }
</style>
</head>
<body>
  <section class="card card-front">
    <div class="name-block">
      <h1 class="person-name">Tom Hollingsworth<span class="surname-end">–Pryce</span></h1>
      <p class="job-title">Operations Manager</p>
    </div>

    <ul class="contact-list">
      <li>
        <svg viewBox="0 0 16 16" aria-hidden="true"><path fill="#c8181e" d="M3 2h3l1 3-2 1.5a8 8 0 0 0 4.5 4.5L11 9l3 1v3a1 1 0 0 1-1 1A11 11 0 0 1 2 3a1 1 0 0 1 1-1z"/></svg>
        <span>(+44) 1632 960 418</span>
      </li>
      <li>
        <svg viewBox="0 0 16 16" aria-hidden="true"><rect x="1" y="3" width="14" height="10" fill="#c8181e"/><path d="M1 3l7 6 7-6" fill="none" stroke="#f7f7f7" stroke-width="1.4"/></svg>
        <span>Tom@keltathletic.co.uk</span>
      </li>
      <li>
        <svg viewBox="0 0 16 16" aria-hidden="true"><g fill="none" stroke="#c8181e" stroke-width="1.3"><circle cx="8" cy="8" r="6.5"/><ellipse cx="8" cy="8" rx="2.8" ry="6.5"/><path d="M1.5 8h13"/></g></svg>
        <span>www.keltathletic.co.uk</span>
      </li>
    </ul>

    <div class="company-mark">
      <span class="mark-dot"></span>
      <span class="mark-name">Kelt Athletic</span>
    </div>

    <div class="brand-row">
      <div class="brand brand-pawaluni"><span class="brand-shape"></span>PawaLuni</div>
      <div class="brand brand-grit"><span class="brand-shape"></span>Grit and Gale</div>
      <div class="brand brand-kelt">Kelt</div>
      <div class="brand brand-verdant"><span class="brand-shape"></span>VerdantFlex</div>
    </div>
  </section>

  <section class="card card-back">
    <div class="back-mark">
      <span class="mark-dot"></span>
      <span class="mark-name">Kelt Athletic</span>
    </div>
  </section>
</body>
</html>
```